Reed & Vale NC grand opening (for BILLBOARD)

Advertising the grand opening of our cannabis/hemp shop in NC. We will sell all things hemp (flower, cartridges, disposables, edibles, creams, lotions, pet products etc...)

Requirements
Must have
• include, open starting Aug 1, but grand opening Aug 15th.
Nice to have
• Difference slogan ideas "Save some cash, buy our grass" "Find your perfect high at Reed & Vale cannabis store" "Experience Nature's Gift: Reed & Vale Cannabis Store"

```html
<!DOCTYPE html>
<html lang="en">
<head>
<meta charset="UTF-8">
<title>Reed &amp; Vale Cannabis Store – Billboard</title>
<link rel="stylesheet" href="https://fonts.googleapis.com/css2?family=Montserrat:ital,wght@0,600;1,600&display=swap">
<style>
  :root {
    --page: #eef0f3;
    --navy-deep: #0d0535;
    --navy-mid: #17125a;
    --blue-haze: #2b3a93;
    --green: #22b14c;
    --green-light: #4fd36b;
    --white: #ffffff;
  }
  * { margin: 0; padding: 0; box-sizing: border-box; }
  html, body {
    width: 1200px;
    height: 1121px;
    overflow: hidden;
    background: var(--page);
  }
  .canvas {
    position: relative;
    width: 1200px;
    height: 1121px;
    display: flex;
    align-items: center;
  }
  .billboard {
    position: relative;
    width: 1200px;
    height: 380px;
    overflow: hidden;
    background: var(--navy-deep);
  }
  .billboard__haze {
    position: absolute;
    inset: 0;
    background:
      radial-gradient(ellipse 60% 55% at 30% 100%, var(--blue-haze) 0%, transparent 70%),
      radial-gradient(ellipse 45% 45% at 75% 100%, var(--blue-haze) 0%, transparent 70%),
      linear-gradient(180deg, var(--navy-deep) 0%, var(--navy-deep) 40%, var(--navy-mid) 100%);
  }
  .billboard__shapes {
    position: absolute;
    inset: 0;
  }
  .billboard__copy {
    position: absolute;
    left: 80px;
    top: 0;
    width: 860px;
    height: 380px;
    display: flex;
    flex-direction: column;
    align-items: center;
    justify-content: center;
    gap: 10px;
    font-family: "Montserrat", sans-serif;
    color: var(--white);
    text-align: center;
  }
  .tagline {
    font-size: 40px;
    line-height: 1.15;
    font-style: italic;
    font-weight: 600;
    letter-spacing: 0.5px;
  }
  .brand-name {
    font-size: 80px;
    line-height: 1.05;
    font-weight: 600;
    white-space: nowrap;
  }
  .store-type {
    font-size: 44px;
    line-height: 1.1;
    font-style: italic;
    font-weight: 600;
    letter-spacing: 0.5px;
  }
  .opening-dates {
    margin-top: 4px;
    font-size: 26px;
    line-height: 1.2;
    font-weight: 600;
    color: var(--green-light);
    letter-spacing: 0.5px;
  }
</style>
</head>
<body>
<main class="canvas">
  <section class="billboard" aria-label="Reed &amp; Vale Cannabis Store billboard">
    <div class="billboard__haze" role="img" aria-label="Soft blue smoke clouds over a deep navy sky"></div>
    <svg class="billboard__shapes" width="1200" height="380" viewBox="0 0 1200 380" aria-hidden="true">
      <defs>
        <linearGradient id="greenPanel" x1="0" y1="0" x2="1" y2="1">
          <stop offset="0" stop-color="#22b14c"/>
          <stop offset="1" stop-color="#4fd36b"/>
        </linearGradient>
      </defs>
      <path class="edge-left" d="M0 0 H22 C60 95 60 285 22 380 H0 Z" fill="var(--green)"/>
      <path class="edge-right" d="M1090 0 H1200 V380 H1000 C950 342 945 256 1000 214 C1060 170 1110 118 1090 0 Z" fill="url(#greenPanel)"/>
    </svg>
    <div class="billboard__copy">
      <p class="tagline">Find your Perfect high at</p>
      <h1 class="brand-name">Reed &amp; Vale</h1>
      <p class="store-type">Cannabis Store</p>
      <p class="opening-dates">Open starting Aug 1 &middot; Grand Opening Aug 15</p>
    </div>
  </section>
</main>
</body>
</html>
```